Zerovan Medical

We are a medical supplier company we sell machines and equipment to all medical sectors in Iraq. Our services include not only the installation of these machines and equipment but also we provide support after installation and we train the staff to use these machines/equipment
We need a website that will make us stand out from our competitors, something professional and catchy
Starting from the home page, before showing the home page we want the loading screen to have our logo animated in a nice way
Then we can proceed to creating the other pages which are
Projects
Services
Training
About
and Contact us
Attached below is our logo and the color blue that we hope to use in the theme of the website
**** In the home page we want to focus on our partners and services****

Target Market(s)

Medical Sector

Industry/Entity Type

Medical

Coding

Coded - Design and coding required

Number of Pages Required

5+ page

Colors
0054AA
0677BA
7BADD7
CADEEF
E8F1F8

Requirements
Must have
• Animation in loading screen or animation in home page
Nice to have
• Some sort of animation for our partners

```html
<!DOCTYPE html>
<html lang="en">
<head>
<meta charset="utf-8">
<title>Zerovan Medical</title>
<link href="https://fonts.googleapis.com/css2?family=Montserrat:wght@400;500;600;700;800&display=swap" rel="stylesheet">
<style>
:root{
  --blue:#0054AA;
  --blue-mid:#0677BA;
  --blue-soft:#7BADD7;
  --blue-pale:#CADEEF;
  --blue-wash:#E8F1F8;
  --ink:#111418;
  --text:#4a4f57;
  --navy:#07162b;
  --white:#fff;
}
*{box-sizing:border-box;margin:0;padding:0}
html,body{width:1200px;height:4376px;overflow:hidden}
body{font-family:'Montserrat',sans-serif;color:var(--ink);background:var(--white);position:relative}
.abs{position:absolute}
.btn{position:absolute;display:flex;align-items:center;justify-content:center;gap:8px;background:var(--blue);color:var(--white);font-size:12px;font-weight:500;letter-spacing:.3px;text-transform:uppercase}
.btn span{font-size:16px;font-weight:400}
.read-more{position:absolute;font-size:12px;font-weight:500;color:var(--blue);text-transform:uppercase}
.section-title{position:absolute;left:0;width:1200px;text-align:center;font-size:32px;font-weight:700}
.title-mark{position:absolute;width:14px;height:14px;border:2px solid var(--blue-mid)}

/* header */
.site-header{position:absolute;top:0;left:0;width:1200px;height:77px;background:var(--white)}
.brand{position:absolute;left:106px;top:22px;display:flex;align-items:center;gap:10px;font-size:24px;font-weight:700;color:var(--navy)}
.brand i{display:block;width:28px;height:28px;border:3px solid var(--blue-mid)}
.nav{position:absolute;top:31px;right:256px;display:flex;gap:38px;font-size:12px;font-weight:500}
.nav a{color:var(--ink);text-decoration:none}
.nav a.active{color:var(--blue)}
.nav-cta{left:981px;top:20px;width:113px;height:38px}

/* hero */
.hero{position:absolute;top:77px;left:0;width:1200px;height:545px;background:linear-gradient(100deg,#0d1f33 0%,#2c4560 40%,#3f6f8e 65%,#2aa3c6 85%,#1b4d6a 100%)}
.hero-frame{position:absolute;left:106px;top:170px;width:30px;height:200px;border:2px solid var(--white);border-right:none}
.hero h1{position:absolute;left:140px;top:145px;color:var(--white);font-size:42px;line-height:52px;font-weight:400}
.hero h1 b{font-weight:700;display:block}
.hero p{position:absolute;left:142px;top:258px;color:var(--white);font-size:18px;line-height:30px;font-weight:500;letter-spacing:.5px}
.hero .btn{left:140px;top:342px;width:165px;height:45px;border:1px solid var(--white)}

/* partners */
.eyebrow{position:absolute;top:688px;left:0;width:1200px;text-align:center;font-size:13px;font-weight:600;letter-spacing:1px}
.eyebrow:before,.eyebrow:after{content:"";display:inline-block;width:20px;height:1px;background:var(--blue);vertical-align:middle;margin:0 10px}
.hex{position:absolute;width:118px;height:134px}
.dots{position:absolute;top:1027px;left:567px;display:flex;gap:8px}
.dots i{width:7px;height:7px;border-radius:50%;background:#d6d9de}
.dots i:first-child{background:var(--blue)}

/* projects */
.projects{position:absolute;top:1107px;left:0;width:1200px;height:648px;background:var(--blue-wash)}
.project-card{position:absolute;top:1268px;width:286px;height:322px;background:linear-gradient(180deg,#c9d3dc,#6f8597 70%,#1c2a38)}
.project-card h3{position:absolute;left:15px;bottom:42px;color:var(--white);font-size:17px;font-weight:700}
.project-card p{position:absolute;left:15px;bottom:18px;color:var(--white);font-size:12px}
.project-card .arrow{position:absolute;right:15px;bottom:18px;width:32px;height:32px;background:var(--blue-mid)}

/* services */
.service-photo{position:absolute;background:linear-gradient(135deg,#a9c9d4,#5d8ea4 55%,#2b4b60)}
.service-frame{position:absolute;border:2px solid var(--blue)}
.service h3{position:absolute;font-size:26px;font-weight:700}
.service p{position:absolute;width:390px;font-size:12.5px;line-height:23px;color:var(--text)}

/* about */
.about{position:absolute;top:3150px;left:0;width:1200px;height:525px;background:var(--blue-wash)}
.about-photo{position:absolute;left:553px;top:3215px;width:505px;height:385px;background:linear-gradient(135deg,#9fb9cf,#5b7f9e 55%,#2f4a64)}

/* catalog */
.catalog{position:absolute;top:3675px;left:0;width:1200px;height:360px;background:var(--blue)}
.catalog h2{position:absolute;top:88px;width:1200px;text-align:center;color:var(--white);font-size:42px;font-weight:400}
.catalog h2 b{font-weight:800}
.catalog p{position:absolute;top:140px;width:1200px;text-align:center;color:var(--white);font-size:15px;line-height:28px}
.catalog .btn{left:503px;top:225px;width:194px;height:46px;border:1px solid var(--white)}

/* footer */
.footer{position:absolute;top:4035px;left:0;width:1200px;height:341px;background:var(--navy);color:var(--white)}
.footer .brand{left:142px;top:68px;color:var(--white);font-size:30px}
.footer .brand i{width:38px;height:38px}
.footer-about{position:absolute;left:142px;top:130px;width:360px;font-size:12px;line-height:22px}
.footer h4{position:absolute;top:86px;font-size:13px;font-weight:600;letter-spacing:.5px}
.links{position:absolute;left:615px;top:120px;list-style:none;font-size:12px;line-height:25px}
.links li:first-child{color:var(--blue-soft)}
.contact-row{position:absolute;left:837px;display:flex;gap:12px;font-size:12px;line-height:18px}
.contact-row svg{flex:none}
.copy{position:absolute;left:142px;top:313px;font-size:11px}
.socials{position:absolute;left:946px;top:304px;display:flex;gap:10px}
.socials i{width:28px;height:28px;border-radius:50%;border:1.5px solid var(--white)}
.socials i:first-child{background:var(--blue-mid);border-color:var(--blue-mid)}
</style>
</head>
<body>

<header class="site-header">
  <div class="brand"><i></i>Zerovan Medical</div>
  <nav class="nav">
    <a class="active">HOME</a><a>PROJECTS</a><a>SERVICES</a><a>TRAINING</a><a>ABOUT US</a>
  </nav>
  <div class="btn nav-cta">Contact us</div>
</header>

<section class="hero" role="img" aria-label="Operating room with patient bed, surgical equipment and monitors">
  <div class="hero-frame" style="top:170px"></div>
  <h1>Empowering<b>Medical Excellence</b></h1>
  <p>YOUR TRUSTED PARTNER FOR MEDICAL<br>EQUIPMENT AND SERVICES</p>
  <div class="btn">Explore more <span>+</span></div>
</section>

<div class="eyebrow">OUR PARTNERS</div>
<svg width="0" height="0" style="position:absolute">
  <defs>
    <filter id="hexShadow" x="-20%" y="-20%" width="140%" height="140%"><feDropShadow dx="0" dy="2" stdDeviation="4" flood-color="#8aa0b8" flood-opacity=".35"/></filter>
    <symbol id="hexBadge" viewBox="0 0 118 134"><polygon points="59,6 110,36 110,98 59,128 8,98 8,36" fill="#fff" filter="url(#hexShadow)"/></symbol>
  </defs>
</svg>
<!-- partner row 1 -->
<svg class="hex" style="left:141px;top:743px"><use href="#hexBadge"/><rect x="30" y="57" width="58" height="20" rx="4" fill="#e21b23"/></svg>
<svg class="hex" style="left:274px;top:743px"><use href="#hexBadge"/><rect x="24" y="59" width="70" height="16" rx="4" fill="#2b3c9a"/></svg>
<svg class="hex" style="left:407px;top:743px"><use href="#hexBadge"/><rect x="26" y="57" width="66" height="20" rx="4" fill="#7d2463"/></svg>
<svg class="hex" style="left:541px;top:743px"><use href="#hexBadge"/><rect x="22" y="59" width="74" height="16" rx="4" fill="#2e7d32"/></svg>
<svg class="hex" style="left:674px;top:743px"><use href="#hexBadge"/><rect x="24" y="53" width="70" height="26" rx="6" fill="#2aa1d8"/></svg>
<svg class="hex" style="left:807px;top:743px"><use href="#hexBadge"/><rect x="28" y="52" width="62" height="30" rx="6" fill="#2f4eaa"/></svg>
<svg class="hex" style="left:941px;top:743px"><use href="#hexBadge"/><rect x="30" y="50" width="58" height="32" rx="6" fill="#c1272d"/></svg>
<!-- partner row 2 -->
<svg class="hex" style="left:208px;top:856px"><use href="#hexBadge"/><rect x="24" y="58" width="70" height="18" rx="4" fill="#1565c0"/></svg>
<svg class="hex" style="left:341px;top:856px"><use href="#hexBadge"/><rect x="26" y="58" width="66" height="18" rx="4" fill="#d0104c"/></svg>
<svg class="hex" style="left:474px;top:856px"><use href="#hexBadge"/><rect x="30" y="50" width="58" height="32" rx="6" fill="#8a9aa6"/></svg>
<svg class="hex" style="left:608px;top:856px"><use href="#hexBadge"/><rect x="26" y="50" width="66" height="32" rx="6" fill="#d62828"/></svg>
<svg class="hex" style="left:741px;top:856px"><use href="#hexBadge"/><rect x="24" y="55" width="70" height="22" rx="5" fill="#3aa655"/></svg>
<svg class="hex" style="left:874px;top:856px"><use href="#hexBadge"/><rect x="26" y="52" width="66" height="28" rx="6" fill="#e04848"/></svg>
<div class="dots"><i></i><i></i><i></i><i></i><i></i></div>

<section class="projects"></section>
<h2 class="section-title" style="top:1170px">Recent Projects</h2>
<div class="title-mark" style="left:593px;top:1221px"></div>
<article class="project-card" style="left:141px" role="img" aria-label="Medical examination equipment with monitor and lamp">
  <h3>PROJECT 01</h3><p>Lorem ipsum dolor sit amet</p>
  <svg class="arrow" viewBox="0 0 32 32"><path d="M11 21 21 11M13 11h8v8" stroke="#fff" stroke-width="1.5" fill="none"/></svg>
</article>
<article class="project-card" style="left:457px" role="img" aria-label="Operating theatre with surgical lights and equipment">
  <h3>PROJECT 02</h3><p>Lorem ipsum dolor sit amet</p>
  <svg class="arrow" viewBox="0 0 32 32"><path d="M11 21 21 11M13 11h8v8" stroke="#fff" stroke-width="1.5" fill="none"/></svg>
</article>
<article class="project-card" style="left:773px" role="img" aria-label="Anaesthesia workstations in a clinical room">
  <h3>PROJECT 03</h3><p>Lorem ipsum dolor sit amet</p>
  <svg class="arrow" viewBox="0 0 32 32"><path d="M11 21 21 11M13 11h8v8" stroke="#fff" stroke-width="1.5" fill="none"/></svg>
</article>
<div class="btn" style="left:518px;top:1625px;width:164px;height:44px">Explore more <span>+</span></div>

<h2 class="section-title" style="top:1817px">Our Services</h2>
<div class="title-mark" style="left:593px;top:1869px"></div>

<div class="service">
  <div class="service-frame" style="left:141px;top:1915px;width:212px;height:210px;border-bottom:none;border-right:none"></div>
  <div class="service-photo" style="left:155px;top:1929px;width:445px;height:304px" role="img" aria-label="Technician installing medical production machinery"></div>
  <svg class="abs" style="left:670px;top:1972px" width="38" height="36" viewBox="0 0 38 36" fill="none" stroke="#0677BA" stroke-width="1.6"><circle cx="19" cy="18" r="11"/><circle cx="19" cy="18" r="5"/><path d="M19 3v4M19 29v4M4 18h4M30 18h4M8 7l3 3M27 26l3 3M30 7l-3 3M11 26l-3 3"/></svg>
  <h3 style="left:670px;top:2018px">Installation</h3>
  <p style="left:670px;top:2062px">Lorem ipsum dolor sit amet, consectetuer adipiscing elit, sed nonummy nibh euismod tincidunt ut laoreet dolore magna aliquam erat volutpat. Ut wisi enim ad minim veniam, quims nostrud exerci commodo consequat.</p>
  <div class="read-more" style="left:670px;top:2171px">Read more +</div>
</div>

<div class="service">
  <svg class="abs" style="left:141px;top:2345px" width="40" height="40" viewBox="0 0 40 40" fill="none" stroke="#0677BA" stroke-width="1.6"><circle cx="14" cy="18" r="6"/><path d="M4 38c0-7 4-11 10-11s10 4 10 11"/><rect x="22" y="2" width="16" height="12" rx="2"/></svg>
  <h3 style="left:141px;top:2400px">Support</h3>
  <p style="left:141px;top:2443px">Lorem ipsum dolor sit amet, consectetuer adipiscing elit, sed nonummy nibh euismod tincidunt ut laoreet dolore magna aliquam erat volutpat. Ut wisi enim ad minim veniam, quims nostrud exerci commodo consequat.</p>
  <div class="read-more" style="left:141px;top:2552px">Read more +</div>
  <div class="service-frame" style="left:847px;top:2297px;width:212px;height:210px;border-bottom:none;border-left:none"></div>
  <div class="service-photo" style="left:600px;top:2310px;width:445px;height:304px" role="img" aria-label="Two technicians operating packaging machinery"></div>
</div>

<div class="service">
  <div class="service-frame" style="left:141px;top:2678px;width:212px;height:210px;border-bottom:none;border-right:none"></div>
  <div class="service-photo" style="left:155px;top:2692px;width:445px;height:304px" role="img" aria-label="Clinical staff being trained on medical monitoring equipment"></div>
  <svg class="abs" style="left:672px;top:2728px" width="42" height="40" viewBox="0 0 42 40" fill="none" stroke="#0677BA" stroke-width="1.6"><rect x="4" y="2" width="22" height="14" rx="2"/><circle cx="8" cy="26" r="4"/><circle cx="21" cy="26" r="4"/><circle cx="34" cy="26" r="4"/><path d="M2 38c0-4 3-6 6-6s6 2 6 6M15 38c0-4 3-6 6-6s6 2 6 6M28 38c0-4 3-6 6-6s6 2 6 6"/></svg>
  <h3 style="left:670px;top:2779px">Training</h3>
  <p style="left:670px;top:2823px">Lorem ipsum dolor sit amet, consectetuer adipiscing elit, sed nonummy nibh euismod tincidunt ut laoreet dolore magna aliquam erat volutpat. Ut wisi enim ad minim veniam, quims nostrud exerci commodo consequat.</p>
  <div class="read-more" style="left:670px;top:2933px">Read more +</div>
</div>
<div class="btn" style="left:526px;top:3031px;width:148px;height:44px">Contact us <span>+</span></div>

<section class="about">
  <h2 class="abs" style="left:142px;top:123px;font-size:32px;font-weight:700">About Zerovan Medical</h2>
  <div class="title-mark" style="left:143px;top:172px"></div>
  <p class="abs" style="left:142px;top:205px;width:360px;font-size:13.5px;line-height:23px;font-weight:600">We are a medical supplier company we sell machines and equipment to all medical sectors in Iraq.</p>
  <p class="abs" style="left:142px;top:285px;width:360px;font-size:12.5px;line-height:21px;color:var(--text)">Our services include not only the installation of these machines and equipment but also we provide support after installation and we train the staff to use these machines/equipment</p>
  <div class="read-more" style="left:142px;top:382px">Read more +</div>
</section>
<div class="about-photo" role="img" aria-label="Clean room with staff working on medical equipment production line"></div>

<section class="catalog">
  <h2>See Our <b>Complete Product Range</b></h2>
  <p>Our extensive range of top-notch general medical supplies can be found in our catalogue.<br>Request a free copy today. All you have to do is fill out the simple form and we will handle the rest.</p>
  <div class="btn">Get free catalog <span>+</span></div>
</section>

<footer class="footer">
  <div class="brand"><i></i>Zerovan Medical</div>
  <p class="footer-about">Our services include not only the installation of these machines and equipment but also we provide support after installation and we train the staff to use these machines/equipment.</p>
  <h4 style="left:615px">QUICK LINKS</h4>
  <ul class="links"><li>Home</li><li>Projects</li><li>Services</li><li>Training</li><li>About Us</li><li>Contact Us</li></ul>
  <h4 style="left:837px">CONTACT DETAILS</h4>
  <div class="contact-row" style="top:126px">
    <svg width="14" height="18" viewBox="0 0 14 18"><path d="M7 1a6 6 0 0 1 6 6c0 4-6 10-6 10S1 11 1 7a6 6 0 0 1 6-6z" fill="#0677BA"/><circle cx="7" cy="7" r="2.2" fill="#07162b"/></svg>
    <span>123, Loream Ipsum Dollar Smit,<br>Nibh Iraq, AB - 123 456</span>
  </div>
  <div class="contact-row" style="top:185px;font-size:15px;font-weight:600;letter-spacing:1px">
    <svg width="14" height="16" viewBox="0 0 14 16"><path d="M3 1l3 3-2 2c1 2 3 4 5 5l2-2 3 3-2 3C6 15-1 8 1 3z" fill="#0677BA"/></svg>
    <span>123 456 7890</span>
  </div>
  <div class="contact-row" style="top:226px">
    <svg width="14" height="14" viewBox="0 0 14 14"><rect x="1" y="3" width="12" height="9" fill="#0677BA"/><path d="M1 3l6 5 6-5" stroke="#07162b" fill="none"/></svg>
    <span>info@zerovanmedical.com</span>
  </div>
  <div class="copy">Copyright 2024 Zerovan Medical. All Rights Reserved.</div>
  <div class="socials"><i></i><i></i><i></i></div>
</footer>

</body>
</html>
```